New Business Card Design Project

We are looking for a talented individual to create a truly awesome/unique business card design for us. We are looking for a someone to design something that will really stand out from the crowd - we don't mind what ideas you come up with (ie embossed/flat/matte/shine etc etc) just wow us with your creativity.
Updates

Target Market(s)

Video Games Industry Professionals (all levels of seniority from QA Testers through to CEOs)

Contact Information for Business Card

Company logo (see upload)
Company name: Northbay Play Careers Ltd
Employee Name: Darren Elsby
Job title: CEO
Website: www.nbpc2go.example
Office +44 1632 960418
Mobile: +44 7700 900276
Email: darren@nbpc2go.example

Colors

Designer to choose colors to be used in the design.

Requirements
Must have
• The business card design MUST contain all the information listed in the BUSINESS CARD DETAILS box.
• You will see the colours that are relevant to us (ie company logo) in the uploaded imagery - however you do not have to use all these colours when designing the business card itself
• MUST BE DOUBLE SIDED

```html
<!DOCTYPE html>
<html lang="en">
<head>
<meta charset="utf-8">
<title>Northbay Play Careers Ltd – Business Card</title>
<link href="https://fonts.googleapis.com/css2?family=Ubuntu:wght@400;500;700&display=swap" rel="stylesheet">
<style>
  :root {
    --stage: #2b2b2d;
    --navy: #1f2d5c;
    --navy-soft: #2b3b72;
    --navy-light: #44558f;
    --orange: #f5822a;
    --white: #ffffff;
    --paper-shade: #eceef3;
    --paper-shade-light: #f6f7fa;
    --social-tile: #3d62a8;
  }
  * { box-sizing: border-box; margin: 0; padding: 0; }
  html, body { width: 1200px; height: 880px; overflow: hidden; }
  body {
    background: var(--stage);
    font-family: "Ubuntu", sans-serif;
    position: relative;
  }
  .card {
    position: absolute;
    width: 620px;
    height: 360px;
    border-radius: 22px;
    overflow: hidden;
    box-shadow: 0 14px 30px rgba(0,0,0,0.45);
  }

  /* Front side */
  .card--front {
    left: 60px;
    top: 60px;
    background: var(--white);
  }
  .front-art {
    position: absolute;
    left: 0;
    top: 60px;
    width: 260px;
    height: 300px;
    border-top-right-radius: 130px;
    background: linear-gradient(160deg, var(--paper-shade) 0%, var(--paper-shade-light) 100%);
  }
  .card--front .brand {
    position: absolute;
    left: 150px;
    top: 150px;
    display: flex;
    align-items: center;
    gap: 18px;
  }
  .brand__mark {
    width: 52px;
    height: 52px;
    border-radius: 50%;
    background: var(--navy);
    flex: none;
  }
  .card--front .brand__name {
    font-weight: 700;
    font-size: 34px;
    line-height: 1.05;
    color: var(--navy);
    letter-spacing: 0.5px;
  }

  /* Back side */
  .card--back {
    left: 520px;
    top: 460px;
    background: var(--navy);
    color: var(--white);
  }
  .back-art {
    position: absolute;
    left: 20px;
    top: 40px;
    width: 250px;
    height: 320px;
    border-radius: 120px 120px 0 0;
    background: linear-gradient(170deg, var(--navy-light) 0%, var(--navy-soft) 100%);
  }
  .card--back .company {
    position: absolute;
    left: 300px;
    top: 46px;
    font-weight: 700;
    font-size: 25px;
    line-height: 1.1;
    color: var(--white);
  }
  .rule {
    position: absolute;
    height: 2px;
    background: var(--orange);
  }
  .rule--company { left: 300px; top: 112px; width: 280px; }
  .person {
    position: absolute;
    left: 300px;
    top: 128px;
  }
  .person__name { font-size: 20px; font-weight: 500; }
  .person__title { font-size: 14px; color: var(--orange); margin-top: 2px; }
  .rule--person { left: 345px; top: 160px; width: 235px; }
  .contacts {
    position: absolute;
    left: 300px;
    top: 188px;
    list-style: none;
    font-size: 13.5px;
    line-height: 1.55;
  }
  .contacts__label { color: var(--orange); }
  .social {
    position: absolute;
    left: 300px;
    top: 280px;
    display: flex;
    gap: 8px;
  }
  .social__tile {
    width: 28px;
    height: 28px;
    border-radius: 3px;
    background: var(--social-tile);
  }
  .web-band {
    position: absolute;
    left: 380px;
    top: 280px;
    width: 240px;
    height: 28px;
    background: var(--orange);
    color: var(--white);
    font-size: 14px;
    font-weight: 500;
    line-height: 28px;
    text-align: right;
    padding-right: 20px;
  }
</style>
</head>
<body>

  <section class="card card--front" aria-label="Card front">
    <div class="front-art" role="img" aria-label="Faint large mascot illustration in pale grey"></div>
    <div class="brand">
      <span class="brand__mark" aria-hidden="true"></span>
      <span class="brand__name">Northbay Play<br>Careers</span>
    </div>
  </section>

  <section class="card card--back" aria-label="Card back">
    <div class="back-art" role="img" aria-label="Large mascot illustration in white and navy"></div>

    <div class="company">Northbay Play<br>Careers Ltd</div>
    <div class="rule rule--company"></div>

    <div class="person">
      <p class="person__name">Darren Elsby</p>
      <p class="person__title">CEO</p>
    </div>
    <div class="rule rule--person"></div>

    <ul class="contacts">
      <li><span class="contacts__label">Office:</span> +44 1632 960418</li>
      <li><span class="contacts__label">Mobile:</span> +44 7700 900276</li>
      <li><span class="contacts__label">Email:</span> darren@nbpc2go.example</li>
    </ul>

    <div class="social" aria-hidden="true">
      <span class="social__tile"></span>
      <span class="social__tile"></span>
    </div>
    <div class="web-band">www.nbpc2go.example</div>
  </section>

</body>
</html>
```